FURLOW MEADOW Pet Resorts Outdoor Signage

4 x 8 outdoor signage design for our two locations

Target Market(s)

Existing and New Customers

Industry/Entity Type

Pet Care

Font styles to use
Sans Serif

Colors

Designer to choose colors to be used in the design.

```html
<!DOCTYPE html>
<html lang="en">
<head>
<meta charset="utf-8">
<title>FURLOW MEADOW Pet Resorts – Outdoor Sign</title>
<link rel="stylesheet" href="https://fonts.googleapis.com/css2?family=Roboto:wght@400;700&family=Roboto+Condensed:wght@700&display=swap">
<style>
  :root {
    --navy: #332f4f;
    --teal: #4a8da3;
    --orange: #f5ab2b;
    --ink: #454545;
    --white: #ffffff;
    --page: #ececec;
    --edge: #d6d6d6;
  }
  * { box-sizing: border-box; margin: 0; padding: 0; }
  html, body { width: 1200px; height: 1200px; overflow: hidden; }
  body {
    background: var(--page);
    font-family: "Roboto", Arial, sans-serif;
    position: relative;
  }
  .sign {
    position: absolute;
    left: 80px; top: 340px;
    width: 1040px; height: 520px;
    background: var(--white);
    border: 1px solid var(--edge);
    overflow: hidden;
  }
  .sign-shapes { position: absolute; inset: 0; width: 100%; height: 100%; }

  .brand {
    position: absolute;
    left: 40px; top: 150px;
    width: 340px;
    display: flex; flex-direction: column; align-items: flex-start; gap: 14px;
  }
  .brand-dot {
    width: 46px; height: 46px; border-radius: 50%;
    background: var(--teal);
  }
  .brand-name {
    font-family: "Roboto", Arial, sans-serif;
    font-weight: 700;
    font-size: 58px;
    line-height: 1.02;
    letter-spacing: 1px;
    color: var(--ink);
  }

  .headline {
    position: absolute; left: 562px; top: 40px;
    font-family: "Roboto Condensed", "Arial Narrow", sans-serif;
    font-weight: 700; font-size: 86px; line-height: 1;
    color: var(--teal); white-space: nowrap;
  }
  .tagline {
    position: absolute; left: 560px; top: 124px;
    font-size: 50px; font-weight: 400; line-height: 1;
    color: var(--white); white-space: nowrap;
  }
  .services {
    position: absolute; display: flex; gap: 22px;
    font-size: 18px; font-weight: 700; color: var(--white);
    white-space: nowrap;
  }
  .services-top { left: 543px; top: 213px; }
  .services-bottom { left: 516px; top: 268px; }
  .service { display: flex; align-items: center; gap: 10px; }
  .service-icon { width: 24px; height: 24px; flex: none; }
  .service-more { color: var(--orange); }

  .phone {
    position: absolute; left: 412px; right: 0; top: 378px;
    text-align: center;
    font-family: "Roboto Condensed", "Arial Narrow", sans-serif;
    font-weight: 700; font-size: 64px; line-height: 1;
    color: var(--white);
  }
  .web {
    position: absolute; left: 412px; right: 0; top: 442px;
    display: flex; align-items: center; gap: 10px;
  }
  .web-rule { flex: 1; height: 4px; background: var(--orange); }
  .web-address {
    font-size: 40px; line-height: 1; color: var(--orange); font-weight: 400;
  }
</style>
</head>
<body>
  <div class="sign">
    <svg class="sign-shapes" viewBox="0 0 1040 520" aria-hidden="true">
      <path d="M430 0 H1040 V520 H412 V362 L518 196 Q566 70 430 0 Z" fill="var(--navy)"/>
      <path d="M440 0 Q548 40 540 180 Q552 40 460 0 Z" fill="var(--teal)"/>
    </svg>

    <div class="brand">
      <span class="brand-dot"></span>
      <p class="brand-name">FURLOW<br>MEADOW</p>
    </div>

    <h1 class="headline">PET RESORT</h1>
    <p class="tagline">All Breed Friendly</p>

    <ul class="services services-top">
      <li class="service"><svg class="service-icon" viewBox="0 0 24 24"><circle cx="12" cy="12" r="12" fill="var(--orange)"/><rect x="6" y="10" width="12" height="4" rx="2" fill="var(--navy)"/></svg>BOARDING</li>
      <li class="service"><svg class="service-icon" viewBox="0 0 24 24"><circle cx="12" cy="12" r="12" fill="var(--orange)"/><rect x="6" y="10" width="12" height="4" rx="2" fill="var(--navy)"/></svg>DAYCARE</li>
      <li class="service"><svg class="service-icon" viewBox="0 0 24 24"><circle cx="12" cy="12" r="12" fill="var(--orange)"/><rect x="6" y="10" width="12" height="4" rx="2" fill="var(--navy)"/></svg>TRAINING FULL</li>
    </ul>
    <ul class="services services-bottom">
      <li class="service"><svg class="service-icon" viewBox="0 0 24 24"><circle cx="12" cy="12" r="12" fill="var(--orange)"/><rect x="6" y="10" width="12" height="4" rx="2" fill="var(--navy)"/></svg>SERVICE SALON</li>
      <li class="service"><svg class="service-icon" viewBox="0 0 24 24"><circle cx="12" cy="12" r="12" fill="var(--orange)"/><rect x="6" y="10" width="12" height="4" rx="2" fill="var(--navy)"/></svg>PET TAXI</li>
      <li class="service service-more"><svg class="service-icon" viewBox="0 0 24 24"><circle cx="12" cy="12" r="12" fill="var(--orange)"/><rect x="6" y="10" width="12" height="4" rx="2" fill="var(--navy)"/></svg>Many more....</li>
    </ul>

    <p class="phone">905-555-0142</p>
    <div class="web">
      <span class="web-rule"></span>
      <span class="web-address">www.furlowmeadow.ca</span>
      <span class="web-rule"></span>
    </div>
  </div>
</body>
</html>
```